TheLedgerMist.com web site

We need a Wordpress theme for a new business we are launching called:

TheLedgerMist.com

"Real time access to currency markets for eCommerce"

You can see the logo / colours at www.theledgermist.com (the logo was designed by a SketchHive.com designer!).

Web site to be along simlar lines to our pre-launch site www.theledgermist.com

The ledger mist is a fintech / financial services company (i.e. the DNA is more tech than financial services) that has three products:

1. SaaS Currency Apps - that customers can use to run their own currency business

2. PaaS Currency API - that customers use to develop their own currency apps and / or integrate currency capabilities into their existing apps and processes

3. Currency Liquidity - direct access to the currency markets to buy/sell currency and make international payments. Forex rates are transparent, consistent and fair for all customers.

Other notes...

A more web 2.0'ish / API related brand, but still serious enough to be take seriously be CxO level decision makers.

The brand is B2B and not B2C or C2C

Please do NOT put forward canned designs found at places like layoutgoblin.com etc.

Reason: Hi,

We have increased the budget for this project - please take another look.

Regards,

Rupert

Hi,

The logo .png file has been uploaded to the design brief

Rupert

Hi,

Some feedback based on what as been submitted so far..

- the logo is designed to go on white background

- take a closer look at our existing "hacked together" site www.theledgermist.com (we like this)- take a look at the site of our owner www.brivanholdings.co.uk- you will notice the sleek, un-cluttered and professional designKindest regards,Rupert

Reason: Just so we get the finishing touches done

Target Market(s)

B2B Targets three main communities:

- financial decision makers
- product managers
- technology/ developer community (for our APIs)

Industry/Entity Type

Financial

Requirements
Must have
• Not appear to be a "blog", but a simple to manage a web site based upon a wordpress theme.

Sections for "product", "blog", "about us", "products"

Clear "call to action" buttons (contact us, sign up etc.) and social buttons

Front page to have a space for video content (as per current web site)

Must have a clear section on the front page "what can we do for you?" where we list various client types and how we can help them

Must have a clear section on the front page "what we do?" where we list the various services we do

```html
<!DOCTYPE html>
<html lang="en">
<head>
<meta charset="utf-8">
<title>TheLedgerMist.com</title>
<link rel="stylesheet" href="https://fonts.googleapis.com/css2?family=Arimo:wght@400;700&family=Open+Sans:wght@400&family=Oswald:wght@500;600&family=Roboto+Slab:wght@500;600&family=Yanone+Kaffeesatz:wght@400&display=swap">
<style>
:root{
  --brand-blue:#1d9be0;
  --band-blue:#0e6aa8;
  --mid-blue:#2e84bd;
  --sky:#6cc0ec;
  --tab-blue:#5fb8ea;
  --ink:#0b1f33;
  --grey-bg:#e9eef0;
  --charcoal:#3a3a3a;
  --card-top:#6a6a6a;
  --card-bot:#2e2e2e;
  --footer:#333333;
  --btn-dark:#0c2c3c;
  --btn-light:#1c5a70;
  --slate:#555b60;
}
*{box-sizing:border-box;margin:0;padding:0}
html,body{width:1023px;height:1200px;overflow:hidden;background:#fff}
body{position:relative;font-family:"Open Sans",sans-serif;color:var(--ink)}
.abs{position:absolute}

/* header */
.site-header{left:0;top:0;width:1023px;height:175px;background:#fff}
.brand{left:33px;top:62px;display:flex;align-items:center;gap:12px;font-family:"Arimo",sans-serif;font-weight:700;font-size:30px;color:var(--slate)}
.brand-dot{width:40px;height:40px;border-radius:50%;background:var(--sky)}
.callout{left:700px;top:47px;width:232px;height:40px;background:#fff;box-shadow:0 0 6px rgba(0,0,0,.25);text-align:center;font-family:"Roboto Slab",serif;font-weight:600;font-size:20px;color:var(--brand-blue);line-height:40px}
.phone{left:710px;top:84px;display:flex;align-items:center;gap:6px;font-family:"Oswald",sans-serif;font-weight:500;font-size:29px;color:var(--slate)}
.main-nav{left:488px;top:139px;height:36px;display:flex}
.nav-tab{position:relative;height:36px;margin-right:-6px;padding:0 20px;display:flex;align-items:center;justify-content:center;font-family:"Arimo",sans-serif;font-size:14px;color:var(--brand-blue);background:linear-gradient(#fbfbfb,#d8dadb);clip-path:polygon(10px 0,calc(100% - 10px) 0,100% 100%,0 100%)}
.nav-tab.is-active{color:#222}

/* blue band */
.band{left:0;top:175px;width:1023px;height:50px;background:var(--band-blue)}
.account{left:14px;top:184px;width:146px;height:32px;background:#1b1b1b;border-radius:4px;color:#fff;font-family:"Arimo",sans-serif;font-size:14px;display:flex;align-items:center;justify-content:center;gap:12px}

/* hero */
.hero{left:0;top:225px;width:1023px;height:350px;background:linear-gradient(#fff 0%,#fff 20%,#b9e1f6 55%,var(--sky) 100%)}
.video{left:16px;top:250px;width:470px;height:298px;background:#000;border:6px solid #5a5a5a;border-radius:6px;box-shadow:0 0 0 1px #222}
.video-caption{left:34px;top:462px;padding:0 14px;height:27px;line-height:27px;background:#2a2a2a;border-radius:3px;color:#ddd;font-family:"Arimo",sans-serif;font-weight:700;font-size:14px}
.video-bar{left:34px;top:496px;width:434px;height:34px;background:#2a2a2a;border-radius:3px;color:#aaa;font-family:"Arimo",sans-serif;font-size:13px}
.hero-title{left:527px;top:230px;font-family:"Yanone Kaffeesatz",sans-serif;font-size:28px;color:var(--brand-blue)}
.dash{height:0;border-top:1px dashed #3aa6e4}
.copy{font-size:10.6px;line-height:17.2px;color:#0b2740}
.copy p+p{margin-top:17px}
.read-more{height:29px;width:90px;padding-left:10px;display:flex;align-items:center;background:linear-gradient(var(--btn-light),var(--btn-dark));color:#fff;font-family:"Arimo",sans-serif;font-size:12px;clip-path:polygon(0 0,80% 0,100% 50%,80% 100%,0 100%);border-radius:3px 0 0 3px}

/* products */
.products{left:0;top:575px;width:1023px;height:208px;background:var(--mid-blue)}
.product{top:635px;width:243px;height:130px;border-radius:6px;background:linear-gradient(var(--card-top),var(--card-bot) 40%);box-shadow:0 1px 3px rgba(0,0,0,.5)}
.product h3{position:absolute;left:15px;top:8px;font-family:"Roboto Slab",serif;font-weight:500;font-size:21px;color:#fff}
.product p{position:absolute;left:7px;top:42px;right:7px;bottom:7px;border:1px solid #888;border-radius:5px;background:#3a3a3a;padding:6px 9px;font-size:10.6px;line-height:17.2px;color:#fff}

/* feature */
.features{left:0;top:783px;width:1023px;height:322px;background:var(--grey-bg)}
.feature-tab{top:808px;width:482px;height:45px;background:var(--tab-blue);clip-path:polygon(0 0,93% 0,100% 100%,0 100%);border-radius:8px 0 0 8px;padding-left:15px;line-height:45px;font-family:"Roboto Slab",serif;font-weight:600;font-size:23px;color:#fff}
.dotline{height:0;border-top:1px dashed #2a6fa0}

/* footer */
.site-footer{left:0;top:1105px;width:1023px;height:95px;background:var(--footer);border-top:2px solid #222}
.legal{left:0;top:1143px;width:1000px;text-align:center;font-size:10.6px;color:#fff}
.follow{left:836px;top:1106px;font-family:"Oswald",sans-serif;font-weight:600;font-size:27px;color:#fff}
.social{left:830px;top:1145px;width:170px;height:45px;border-radius:6px;background:#8cc8f0;box-shadow:0 0 6px #8cd4ff;display:flex;gap:7px;align-items:center;justify-content:center}
.social span{width:25px;height:25px;border-radius:4px;background:#2f6d9a}
</style>
</head>
<body>

<header class="site-header abs">
  <div class="brand abs"><span class="brand-dot"></span>TheLedgerMist.com</div>
  <div class="callout abs">Any Queries? Call Us</div>
  <div class="phone abs">
    <svg width="26" height="26" viewBox="0 0 26 26" aria-hidden="true"><circle cx="13" cy="13" r="13" fill="#1d9be0"/><path d="M9 6c1.5-.5 2.5 2 3 3.5.3 1-1 1.5-1 2.3.2 1.5 1.7 3.3 3 4 .8.3 1.5-1 2.4-.8 1.3.4 3.8 1.6 3.3 3-1 2-3 2.3-4.8 1.5C11 18 8 14.8 7 11c-.5-2 .3-4.2 2-5z" fill="#fff"/></svg>
    888 555 0147
  </div>
  <nav class="main-nav abs">
    <a class="nav-tab is-active" style="width:98px">Home</a>
    <a class="nav-tab" style="width:96px">About Us</a>
    <a class="nav-tab" style="width:96px">Products</a>
    <a class="nav-tab" style="width:94px">Blog</a>
    <a class="nav-tab" style="width:100px">Contact Us</a>
  </nav>
</header>

<div class="band abs"></div>
<div class="account abs"><span>Sign in</span><span>I</span><span>Register</span></div>

<section class="hero abs"></section>
<svg class="abs" style="left:490px;top:188px" width="533" height="38" viewBox="0 0 533 38" aria-hidden="true"><path d="M0 38 C20 38 28 2 60 2 L465 2 C495 2 505 30 533 30 L533 38 Z" fill="#fff"/></svg>

<div class="video abs"></div>
<svg class="abs" style="left:205px;top:350px" width="84" height="84" viewBox="0 0 84 84" aria-hidden="true">
  <circle cx="42" cy="42" r="41" fill="#2b2b2b"/>
  <circle cx="42" cy="42" r="36" fill="none" stroke="#8a8a8a" stroke-width="6"/>
  <circle cx="42" cy="42" r="28" fill="#6e6e6e"/>
  <text x="42" y="46" text-anchor="middle" font-family="Arimo, sans-serif" font-weight="700" font-size="11" fill="#fff">PLAY</text>
</svg>
<div class="video-caption abs">Intro to TheLedgerMist.com (only 1.5 mins!)</div>
<div class="video-bar abs">
  <svg class="abs" style="left:18px;top:9px" width="12" height="16" viewBox="0 0 12 16" aria-hidden="true"><path d="M0 0 L12 8 L0 16 Z" fill="#777"/></svg>
  <span class="abs" style="left:45px;top:9px">0:00</span>
  <span class="abs" style="left:86px;top:12px;width:254px;height:10px;background:#555;border-radius:2px"></span>
  <span class="abs" style="left:82px;top:8px;width:12px;height:17px;background:#aaa;border-radius:2px"></span>
  <span class="abs" style="left:353px;top:9px">1:28</span>
  <svg class="abs" style="left:393px;top:7px" width="22" height="20" viewBox="0 0 22 20" aria-hidden="true"><rect x="0" y="12" width="5" height="8" fill="#777"/><rect x="8" y="6" width="5" height="14" fill="#777"/><rect x="16" y="0" width="5" height="20" fill="#777"/></svg>
</div>

<h1 class="hero-title abs">Real time access to currency markets for eCommerce</h1>
<div class="dash abs" style="left:527px;top:269px;width:476px"></div>
<div class="copy abs" style="left:527px;top:285px;width:470px">
  <p>Lorem ipsum dolor sit amet, consectetur adipiscing elit. Sed molestie aliquam enim, at vulputate eros sagittis eu. Morbi et ultrices nisi. Aliquam fermentum bibendum libero, in posuere erat porta nec. Sed id gravida urna. Nullam auctor volutpat tellus in lacinia. In hac habitasse platea dictumst.</p>
  <p>Nullam mollis metus neque, at consectetur diam. Curabitur consectetur lacus turpis. Integer vel quam ipsum, at volutpat metus. Quisque ullamcorper purus molestie purus luctus interdum. In gravida fringilla nulla in semper. Vestibulum faucibus ullamcorper sapien ut porttitor. Integer non dapibus nibh. In sollicitudin tellus id sapien porttitor fermentum. Proin et elit eu ipsum tincidunt gravida.</p>
</div>
<div class="dash abs" style="left:527px;top:514px;width:476px"></div>
<a class="read-more abs" style="left:528px;top:535px">Read More</a>

<section class="products abs"></section>
<article class="product abs" style="left:8px"><h3>SaaS Currency Apps</h3><p>That customers can use to run their own currency business</p></article>
<article class="product abs" style="left:262px"><h3>PaaS Currency API</h3><p>That customers use to develop their own currency apps and / or integrate currency capabilities into their existing apps and processes</p></article>
<article class="product abs" style="left:516px"><h3>Currency Liquidity</h3><p>direct access to the currency markets to buy/sell currency and make international payments. Forex rates are transparent, consistent and fair for all customers.</p></article>
<article class="product abs" style="left:770px"><h3>FX Market Data</h3><p>Lorem ipsum dolor sit amet nuno di valencia es ta de mario ed psania.</p></article>

<section class="features abs"></section>
<h2 class="feature-tab abs" style="left:9px">What can we do for you?</h2>
<h2 class="feature-tab abs" style="left:519px">What we do?</h2>
<div class="copy abs" style="left:14px;top:868px;width:475px;height:140px;overflow:hidden">
  <p>Lorem ipsum dolor sit amet, consectetur adipiscing elit. Sed molestie aliquam enim, at vulputate eros sagittis eu. Morbi et ultrices nisi. Aliquam fermentum bibendum libero, in posuere erat porta nec. Sed id gravida urna. Nullam auctor volutpat tellus in lacinia. In hac habitasse platea dictumst.</p>
  <p>Nullam mollis metus neque, at consectetur diam. Curabitur consectetur lacus turpis. Integer vel quam ipsum, at volutpat metus. Quisque ullamcorper purus molestie purus luctus interdum. In gravida fringilla nulla in semper. Vestibulum faucibus ullamcorper sapien ut porttitor. Integer non</p>
</div>
<div class="copy abs" style="left:525px;top:868px;width:475px;height:140px;overflow:hidden">
  <p>Lorem ipsum dolor sit amet, consectetur adipiscing elit. Sed molestie aliquam enim, at vulputate eros sagittis eu. Morbi et ultrices nisi. Aliquam fermentum bibendum libero, in posuere erat porta nec. Sed id gravida urna. Nullam auctor volutpat tellus in lacinia. In hac habitasse platea dictumst.</p>
  <p>Nullam mollis metus neque, at consectetur diam. Curabitur consectetur lacus turpis. Integer vel quam ipsum, at volutpat metus. Quisque ullamcorper purus molestie purus luctus interdum. In gravida fringilla nulla in semper. Vestibulum faucibus ullamcorper sapien ut porttitor. Integer non</p>
</div>
<div class="dotline abs" style="left:12px;top:1038px;width:477px"></div>
<div class="dotline abs" style="left:523px;top:1038px;width:477px"></div>
<a class="read-more abs" style="left:13px;top:1052px">Read More</a>
<a class="read-more abs" style="left:523px;top:1052px">Read More</a>

<footer class="site-footer abs"></footer>
<p class="legal abs">©2011, All Rights Reserved, www.theledgermist.com</p>
<div class="follow abs">Follow us on</div>
<div class="social abs" aria-label="Social links">
  <span></span><span></span><span></span><span></span><span></span>
</div>

</body>
</html>
```